Emergency Medical Training and Events Company Business Needs Business Card Design

We are in need of a business card for our dynamic company expanding its customer base and need to be easily contacted and identified for when we visit with government officials, potential EMS / Fire agencies and county coordinators to arrange for training programs for first responders to better prepare them for critical thinking at critical incidents.

Target Market(s)

EMS/Fire and Event Promoters

Industry/Entity Type

Medical

Contact Information for Business Card

Two cards, comparable designs:

Martin K. Halvey, Principal, m.halvey@rvqtlo.com
Owen Tash, Event and Training Specialist, o.tash@rvqtlo.com

Font styles to use
Other font styles liked:
• Cambria

Colors

Designer to choose colors to be used in the design.

Requirements
Must have
• Company Logo, Spots for Name, Title, Phone Number, Email, Website
• A bullet list stating that we offer, QRB CPR and First Aid Instructors, Hold the Line Instructors, Event EMS, CME's, MCI Training and Planning. We prefer to have a black background for the card but if you can make a blue or white card stand out we would review that as well.
Should not have
• Tacky logos or special sayings ... simple, elegant, professional is the look we seek

```html
<!DOCTYPE html>
<html lang="en">
<head>
<meta charset="utf-8">
<title>RVQ Training Co. – Business Card</title>
<link rel="stylesheet" href="https://fonts.googleapis.com/css2?family=Lato:wght@400;700&display=swap">
<style>
  :root {
    --stage: #d8d8da;
    --card: #0b1a4f;
    --card-mark: #15265e;
    --red: #d4242a;
    --ink: #e8eaf1;
    --white: #ffffff;
  }
  * { box-sizing: border-box; margin: 0; padding: 0; }
  html, body {
    width: 1200px; height: 1200px; overflow: hidden;
    background: var(--stage);
    font-family: "Lato", Arial, sans-serif;
    color: var(--ink);
  }
  .card {
    position: absolute; left: 270px; width: 661px; height: 378px;
    background: var(--card); overflow: hidden;
  }
  .card--front { top: 170px; border-radius: 0 31px 0 31px; }
  .card--back  { top: 626px; border-radius: 31px 0 31px 0; }

  .card__mark {
    position: absolute; right: -120px; top: 40px;
    width: 300px; height: 300px; border-radius: 50%;
    background: var(--card-mark);
  }

  .brand {
    position: absolute; left: 67px; display: flex; align-items: center; gap: 12px;
  }
  .brand__dot { width: 34px; height: 34px; border-radius: 50%; background: var(--red); }
  .brand__name {
    font-weight: 700; font-size: 27px; color: var(--white); letter-spacing: 0.5px;
    white-space: nowrap;
  }
  .card--front .brand { top: 145px; }
  .card--back .brand { top: 172px; }

  .divider { position: absolute; left: 330px; width: 3px; background: var(--white); }
  .card--front .divider { top: 76px; height: 172px; }
  .card--back .divider { top: 149px; height: 81px; }

  .contact { position: absolute; left: 370px; top: 72px; }
  .contact__name { font-size: 23px; font-weight: 400; color: var(--white); letter-spacing: 0.3px; line-height: 1.1; }
  .contact__name strong { color: var(--red); font-weight: 700; }
  .contact__title { font-size: 16px; margin-top: 3px; }
  .contact__address { font-size: 16px; line-height: 21px; margin-top: 12px; }
  .contact__list { list-style: none; margin-top: 10px; }
  .contact__item { display: flex; align-items: center; font-size: 17px; height: 23px; }
  .icon { width: 14px; height: 14px; margin-right: 9px; flex: none; }

  .offer { position: absolute; left: 22px; top: 306px; }
  .offer__heading { font-size: 18px; font-weight: 700; color: var(--red); }
  .offer__list { display: flex; list-style: none; margin-top: 9px; font-size: 15px; white-space: nowrap; }
  .offer__list li + li::before { content: "|"; margin: 0 13px; }

  .web-large {
    position: absolute; left: 368px; top: 172px; display: flex; align-items: center;
    font-size: 24px;
  }
  .web-large .icon { width: 16px; height: 16px; margin-right: 12px; }
</style>
</head>
<body>

<section class="card card--front" aria-label="Business card front">
  <div class="card__mark" aria-hidden="true"></div>
  <div class="brand">
    <span class="brand__dot"></span>
    <span class="brand__name">RVQ Training Co.</span>
  </div>
  <div class="divider"></div>
  <div class="contact">
    <h1 class="contact__name"><strong>MARTIN K.</strong> HALVEY</h1>
    <p class="contact__title">Principal</p>
    <p class="contact__address">PO Box 417 Harlow Falls,<br>New York, USA</p>
    <ul class="contact__list">
      <li class="contact__item">
        <svg class="icon" viewBox="0 0 14 14"><rect x="3.5" y="0.8" width="7" height="12.4" rx="1.2" fill="none" stroke="#d4242a" stroke-width="1.4"/><circle cx="7" cy="11" r="0.8" fill="#d4242a"/></svg>
        555 014 2290
      </li>
      <li class="contact__item">
        <svg class="icon" viewBox="0 0 14 14"><rect x="0.5" y="3" width="13" height="9" fill="#d4242a"/><path d="M0.5 3 L7 8 L13.5 3" fill="none" stroke="#0b1a4f" stroke-width="1.2"/></svg>
        m.halvey@rvqtlo.com
      </li>
      <li class="contact__item">
        <svg class="icon" viewBox="0 0 14 14" fill="none" stroke="#d4242a" stroke-width="1.1"><circle cx="7" cy="7" r="6"/><ellipse cx="7" cy="7" rx="2.6" ry="6"/><path d="M1 7h12M2 4h10M2 10h10"/></svg>
        www.rvqtlo.com
      </li>
    </ul>
  </div>
  <div class="offer">
    <h2 class="offer__heading">We Offer</h2>
    <ul class="offer__list">
      <li>Training Planning</li>
      <li>CPR/AED Training</li>
      <li>First Aid Training</li>
      <li>EMS Event Management</li>
    </ul>
  </div>
</section>

<section class="card card--back" aria-label="Business card back">
  <div class="card__mark" aria-hidden="true"></div>
  <div class="brand">
    <span class="brand__dot"></span>
    <span class="brand__name">RVQ Training Co.</span>
  </div>
  <div class="divider"></div>
  <p class="web-large">
    <svg class="icon" viewBox="0 0 14 14" fill="none" stroke="#d4242a" stroke-width="1.1"><circle cx="7" cy="7" r="6"/><ellipse cx="7" cy="7" rx="2.6" ry="6"/><path d="M1 7h12M2 4h10M2 10h10"/></svg>
    www.rvqtlo.com
  </p>
</section>

</body>
</html>
```